Occupational Therapy Clinic Advertisement

Create an advertisement for a magazine. Below I have attached my original ad (Ad 2020.pdf) . I want the ad changed and it should be eye catching. I would like a eye catching graphics added in the ad. It should be a graphic image that applies to education. I am attaching a sample graphic image of that I liked from someone elses ad- it should not be the same- it just is there to show what I like. Please use the same words from my original ad.Dimensions: 3.75in x 10.3 in

Target Market(s)

Parents of School aged children

Requirements
Must have
• Must have eye catching Graphic. Colors should be eye catching for a typed magazine.

```html
<!DOCTYPE html>
<html lang="en">
<head>
<meta charset="utf-8">
<title>Bright Path OT Services</title>
<link rel="stylesheet" href="https://fonts.googleapis.com/css2?family=Barlow:wght@400;500;600;700;800&family=Barlow+Condensed:wght@500;600;700&family=Open+Sans:wght@400;600&display=swap">
<style>
  :root {
    --orange-band: #cf5529;
    --gold: #ffc20e;
    --blush: #f9d9cc;
    --teal: #1aa9b6;
    --red: #e0452b;
    --brown: #8b4129;
    --headline-red: #e8381f;
    --purple: #6f3a96;
    --amber: #e09c24;
    --green: #4fa886;
    --ink: #555555;
    --rule: #8a8a8a;
    --paper: #f1f0ee;
    --soft-yellow: #fbf3c4;
  }
  * { margin: 0; padding: 0; box-sizing: border-box; }
  html, body { width: 1200px; height: 3095px; overflow: hidden; background: #ffffff; }
  .canvas { position: relative; width: 1200px; height: 3095px; background: #ffffff; font-family: "Barlow", sans-serif; }
  .ad { position: absolute; left: 56px; top: 56px; width: 1084px; height: 2980px;
        background: linear-gradient(180deg, var(--paper) 0%, #ffffff 40%, #ffffff 55%, var(--paper) 100%);
        border: 1px solid #cfcfcf; }
  .abs { position: absolute; }

  .header-band { left: 56px; top: 56px; width: 1084px; height: 326px; background: var(--orange-band); }
  .brand-mark { left: 154px; top: 128px; width: 172px; height: 172px; background: #f6f3f0; border-radius: 22px; }
  .brand-name { left: 356px; top: 118px; font-family: "Barlow", sans-serif; font-weight: 800; font-size: 94px; line-height: 1; color: var(--gold); letter-spacing: 2px; }
  .brand-sub { left: 356px; top: 220px; font-family: "Barlow Condensed", sans-serif; font-weight: 600; font-size: 72px; line-height: 1; color: var(--blush); }

  .question { font-size: 54px; line-height: 68px; color: #ffffff; letter-spacing: 1px; font-weight: 500; }
  .question strong { font-weight: 800; }
  .q-reading { left: 518px; top: 382px; width: 550px; height: 252px; background: var(--teal); border-radius: 0 0 12px 12px; padding: 24px 0 0 34px; z-index: 3; }
  .q-test { left: 518px; top: 624px; width: 550px; height: 274px; background: var(--red); border-radius: 12px; padding: 30px 0 0 34px; z-index: 2; box-shadow: 0 -4px 0 rgba(0,0,0,0.12); }
  .q-names { left: 132px; top: 882px; width: 936px; height: 228px; background: var(--brown); border-radius: 12px; padding: 44px 0 0 56px; z-index: 1; }

  .study-art { left: 142px; top: 482px; width: 318px; height: 318px; border-radius: 50%;
               background: radial-gradient(circle at 50% 70%, #d99a6e 0%, #e7b48c 45%, #f1f0ee 72%); }

  .ornament-area { left: 56px; top: 1140px; width: 1084px; height: 700px;
                   background: radial-gradient(ellipse at 80% 40%, var(--soft-yellow) 0%, rgba(251,243,196,0) 60%); }
  .graduate-art { left: 714px; top: 1146px; width: 332px; height: 512px; border-radius: 40px;
                  background: linear-gradient(160deg, #3d3f7a 0%, #c8332a 60%, #f1f0ee 100%); opacity: 0.9; }

  .headline { right: 526px; text-align: right; font-family: "Barlow", sans-serif; font-weight: 800; color: var(--headline-red); line-height: 1; }
  .h1 { top: 1274px; font-size: 68px; }
  .h2 { top: 1346px; font-size: 94px; }
  .h2 .struck { position: relative; color: var(--headline-red); margin-right: 18px; }
  .h2 .struck::after { content: ""; position: absolute; left: -38px; right: -28px; top: 44%; height: 6px; background: #3a2a2a; transform: rotate(9deg); }
  .h2 .struck::before { content: ""; position: absolute; left: -38px; right: -28px; top: 44%; height: 6px; background: #3a2a2a; transform: rotate(-7deg); }
  .h3 { top: 1432px; font-size: 100px; }
  .h4 { top: 1526px; font-size: 106px; }

  .feature { left: 240px; width: 818px; height: 164px; border-radius: 0 16px 16px 0; color: #ffffff; padding: 20px 0 0 74px; font-family: "Barlow", sans-serif; font-size: 50px; line-height: 60px; font-weight: 500; }
  .feature strong { font-weight: 800; }
  .feature-evaluate { top: 1860px; background: var(--purple); }
  .feature-method { top: 2036px; background: var(--amber); }
  .feature-deficits { top: 2212px; background: var(--green); }
  .feature-badge { width: 158px; height: 158px; border-radius: 50%; border: 6px solid #ffffff; display: flex; align-items: center; justify-content: center; }
  .badge-evaluate { left: 135px; top: 1857px; background: var(--purple); }
  .badge-method { left: 135px; top: 2033px; background: var(--amber); }
  .badge-deficits { left: 135px; top: 2209px; background: var(--green); }

  .ages { right: 143px; top: 2390px; font-family: "Barlow", sans-serif; font-size: 50px; font-weight: 500; color: var(--purple); }
  .rule { height: 2px; background: var(--rule); }
  .rule-1 { left: 108px; top: 2468px; width: 980px; }
  .rule-2 { left: 108px; top: 2540px; width: 980px; }
  .rule-3 { left: 198px; top: 2810px; width: 888px; }
  .rsa { left: 108px; top: 2478px; font-family: "Barlow", sans-serif; font-size: 50px; font-weight: 500; color: var(--orange-band); }

  .contact-icon { width: 70px; height: 70px; }
  .icon-pin { left: 104px; top: 2576px; }
  .icon-mail { left: 104px; top: 2688px; }
  .icon-phone { left: 108px; top: 2886px; }
  .contact-text { left: 198px; font-family: "Barlow", sans-serif; font-size: 40px; line-height: 50px; color: var(--ink); font-weight: 500; }
  .location { top: 2566px; letter-spacing: 0.3px; }
  .email-line { top: 2678px; font-family: "Open Sans", sans-serif; font-size: 36px; line-height: 49px; letter-spacing: -0.5px; }
  .email-line .email { color: var(--orange-band); font-family: "Barlow", sans-serif; font-size: 40px; font-weight: 500; letter-spacing: 0; }
  .therapist { left: 200px; top: 2830px; font-family: "Barlow", sans-serif; font-size: 52px; font-weight: 500; color: var(--headline-red); }
  .phone { left: 198px; top: 2888px; font-family: "Barlow", sans-serif; font-size: 66px; font-weight: 500; color: var(--ink); letter-spacing: 2px; }
</style>
</head>
<body>
<div class="canvas">
  <div class="ad"></div>

  <header>
    <div class="abs header-band"></div>
    <div class="abs brand-mark"></div>
    <div class="abs brand-name">BRIGHT PATH</div>
    <div class="abs brand-sub">OT SERVICES</div>
  </header>

  <div class="abs study-art" role="img" aria-label="Illustration of a worried boy reading at a desk with books and a lamp"></div>

  <div class="abs question q-reading">DOES YOUR CHILD<br>STRUGGLE WITH<br><strong>READING/KRIAH?</strong></div>
  <div class="abs question q-test">KNOWS THE<br>INFORMATION BUT<br><strong>FAILS THE TEST?</strong></div>
  <div class="abs question q-names">HAS DIFFICULTY REMEMBERING<br><strong>NAMES AND DATES?</strong></div>

  <div class="abs ornament-area" role="img" aria-label="Decorative yellow swirl lines with dots and chevrons"></div>

  <div class="abs headline h1">YES YOUR CHILD</div>
  <div class="abs headline h2"><span class="struck">CAN</span>WILL</div>
  <div class="abs headline h3">SUCCEED</div>
  <div class="abs headline h4">IN SCHOOL!</div>

  <div class="abs graduate-art" role="img" aria-label="Illustration of a graduate in cap and red cape flying upward"></div>

  <div class="abs feature feature-evaluate"><strong>We Evaluate</strong><br>Using standardized Evaluations</div>
  <div class="abs feature feature-method"><strong>We Treat</strong>&nbsp; Using Researched<br>based techniques</div>
  <div class="abs feature feature-deficits"><strong>We Treat</strong> the underlying<br>processing deficits</div>

  <div class="abs feature-badge badge-evaluate">
    <svg width="84" height="84" viewBox="0 0 84 84" fill="#fff">
      <rect x="18" y="50" width="12" height="26" rx="3"/>
      <rect x="36" y="40" width="12" height="36" rx="3"/>
      <rect x="54" y="28" width="12" height="48" rx="3"/>
      <path d="M8 44 L44 18" stroke="#fff" stroke-width="6" stroke-linecap="round"/>
      <path d="M36 12 L54 10 L48 28 Z"/>
    </svg>
  </div>
  <div class="abs feature-badge badge-method">
    <svg width="90" height="90" viewBox="0 0 90 90" fill="none" stroke="#fff" stroke-width="6" stroke-linejoin="round">
      <path d="M14 22 L26 10 L74 58 L80 80 L58 74 Z"/>
      <path d="M20 28 L32 16"/>
    </svg>
  </div>
  <div class="abs feature-badge badge-deficits">
    <svg width="96" height="96" viewBox="0 0 96 96" fill="#fff">
      <circle cx="48" cy="20" r="9"/><path d="M34 42 a14 12 0 0 1 28 0 Z"/>
      <circle cx="24" cy="54" r="9"/><path d="M10 76 a14 12 0 0 1 28 0 Z"/>
      <circle cx="72" cy="54" r="9"/><path d="M58 76 a14 12 0 0 1 28 0 Z"/>
      <path d="M22 38 a28 28 0 0 1 10 -14 M74 38 a28 28 0 0 0 -10 -14 M36 86 a30 30 0 0 0 24 0" fill="none" stroke="#fff" stroke-width="3"/>
    </svg>
  </div>

  <div class="abs ages">Ages: 6-18</div>
  <div class="abs rule rule-1"></div>
  <div class="abs rsa">Board of Ed OT RSA's accepted</div>
  <div class="abs rule rule-2"></div>

  <svg class="abs contact-icon icon-pin" viewBox="0 0 70 70" fill="none" stroke="#666" stroke-width="2.5">
    <circle cx="35" cy="35" r="32"/>
    <path d="M35 54 C26 42 22 36 22 29 a13 13 0 0 1 26 0 C48 36 44 42 35 54 Z"/>
    <circle cx="35" cy="29" r="5"/>
  </svg>
  <div class="abs contact-text location">Located in Borough Park<br>Evaluations done in Borough Park &amp; Staten Island</div>

  <svg class="abs contact-icon icon-mail" viewBox="0 0 70 70" fill="none" stroke="#666" stroke-width="2.5">
    <circle cx="35" cy="35" r="32"/>
    <rect x="20" y="25" width="30" height="20" fill="#666"/>
    <path d="M20 25 L35 37 L50 25 M20 45 L31 34 M50 45 L39 34" stroke="#fff" stroke-width="2"/>
  </svg>
  <div class="abs contact-text email-line">For more information or to be added to our email list,<br>please email: <span class="email">brightpathot@example.com</span></div>

  <div class="abs rule rule-3"></div>
  <div class="abs therapist">Dina Halvorsen OTR/L</div>
  <svg class="abs contact-icon icon-phone" viewBox="0 0 70 70" fill="none" stroke="#666" stroke-width="2.5">
    <circle cx="35" cy="35" r="32"/>
    <path d="M24 18 l8 -2 l5 11 l-5 4 c2 6 6 10 12 12 l4 -5 l11 5 l-2 8 c-16 2 -34 -16 -33 -33 Z"/>
  </svg>
  <div class="abs phone">(718)555-0142</div>
</div>
</body>
</html>
```